One Page Sales Flyer for Wireless Survey- Computer Hardware

I want a designer to create a one page 4 color sales slick to be given to our sales team to sell to the end customers. I would like a visual picture of a heat map so zavvix "heat map wireless" to get an idea of how that image should look.

```html
<!DOCTYPE html>
<html lang="en">
<head>
<meta charset="utf-8">
<title>Wireless Site Survey Sales Flyer</title>
<link href="https://fonts.googleapis.com/css2?family=Bebas+Neue&family=Montserrat:wght@400;500;600;700&display=swap" rel="stylesheet">
<style>
  :root {
    --page-bg: #e8e8e8;
    --paper: #ffffff;
    --ink: #333333;
    --ink-dark: #1d1d1d;
    --blue: #2f9ee6;
    --blue-bright: #3fb2f2;
    --black: #0c0c0c;
    --bar-dark: #3b3b3b;
    --heat-purple: #4a2350;
    --heat-teal: #2c5a5a;
    --heat-olive: #7c7a22;
  }
  * { box-sizing: border-box; margin: 0; padding: 0; }
  html, body { width: 762px; height: 1200px; overflow: hidden; background: var(--page-bg); }
  body { position: relative; font-family: "Montserrat", Arial, sans-serif; color: var(--ink); }

  .flyer {
    position: absolute; left: 20px; top: 40px; width: 722px; height: 1120px;
    background: var(--paper); overflow: hidden;
    box-shadow: 0 2px 10px rgba(0,0,0,0.15);
  }

  .hero-heatmap {
    position: absolute; left: 0; top: 0; width: 722px; height: 380px;
    background:
      radial-gradient(circle at 20% 30%, rgba(124,122,34,0.85) 0 14%, transparent 32%),
      radial-gradient(circle at 62% 75%, rgba(44,90,90,0.9) 0 16%, transparent 36%),
      radial-gradient(circle at 85% 20%, rgba(124,122,34,0.7) 0 12%, transparent 30%),
      radial-gradient(circle at 40% 85%, rgba(124,122,34,0.8) 0 12%, transparent 28%),
      linear-gradient(135deg, var(--heat-purple), var(--heat-teal) 45%, var(--heat-olive) 70%, var(--heat-purple));
  }
  .source-note {
    position: absolute; right: 30px; top: 52px;
    font-size: 6.5px; font-weight: 600; color: #f2f2f2;
  }
  .headline {
    position: absolute; left: 102px; top: 126px;
    font-family: "Bebas Neue", "Arial Narrow", sans-serif; font-weight: 400; line-height: 1.0;
  }
  .headline .lead { display: block; color: var(--blue-bright); font-size: 48px; }
  .headline .sub { display: block; color: #ffffff; font-size: 45px; }

  .target-title {
    position: absolute; left: 425px; top: 311px; width: 297px; height: 69px;
    background: var(--black); border-top: 8px solid var(--blue-bright);
    color: #ffffff; font-family: "Bebas Neue", "Arial Narrow", sans-serif;
    font-size: 34px; line-height: 61px; padding-left: 26px;
  }
  .target-list {
    position: absolute; left: 433px; top: 380px; width: 260px; height: 430px;
    background: var(--blue-bright); border-radius: 0 0 18px 18px;
    list-style: none; padding: 18px 22px 0 22px;
  }
  .target-list li {
    display: flex; align-items: center; gap: 10px;
    height: 37px; border-bottom: 1px solid rgba(255,255,255,0.25);
    color: #ffffff; font-size: 14.5px; font-weight: 600;
  }
  .target-list li:last-child { border-bottom: none; }
  .target-list svg { width: 14px; height: 14px; flex: none; }

  .info-column { position: absolute; left: 18px; top: 420px; width: 400px; }
  .info-block { margin-bottom: 46px; }
  .info-block h2 {
    font-size: 13px; font-weight: 700; color: var(--ink-dark);
    border-left: 6px solid var(--blue-bright); padding-left: 10px; line-height: 20px;
    margin-bottom: 14px;
  }
  .info-block p, .info-block li {
    font-size: 11.5px; line-height: 1.45; padding-left: 16px;
  }
  .info-block ol { list-style: none; }
  .info-block li { margin-bottom: 14px; }
  .info-block li b { font-weight: 700; }

  .brand { position: absolute; left: 425px; top: 845px; width: 297px; text-align: center; }
  .brand-mark {
    width: 82px; height: 82px; margin: 0 auto 20px; background: var(--blue);
  }
  .brand-name {
    font-size: 36px; font-weight: 500; letter-spacing: 2px; color: var(--ink-dark);
    margin-bottom: 10px;
  }
  .brand-contact { font-size: 13.5px; font-weight: 700; color: var(--ink-dark); line-height: 1.45; }
  .brand-phone { font-size: 21px; font-weight: 700; color: var(--blue); }

  .footer-bar { position: absolute; left: 0; bottom: 0; width: 722px; height: 10px; display: flex; }
  .footer-bar .dark { width: 260px; background: var(--bar-dark); }
  .footer-bar .blue { flex: 1; background: var(--blue-bright); }
</style>
</head>
<body>
<main class="flyer">
  <div class="hero-heatmap" role="img" aria-label="Colourful wireless signal heat map in purple, teal and yellow-green tones"></div>
  <p class="source-note">*Northfield IT Panel, "Office Network Health Study", 2018</p>
  <h1 class="headline">
    <span class="lead">Increase Hardware and Services</span>
    <span class="sub">Spend with Wireless Site Surveys</span>
  </h1>

  <div class="target-title">Target Customers</div>
  <ul class="target-list">
    <li><svg viewBox="0 0 14 14"><rect x="1" y="4" width="9" height="6" fill="#fff"/><rect x="10" y="6" width="3" height="4" fill="#fff"/></svg>Distributors</li>
    <li><svg viewBox="0 0 14 14"><path d="M1 6 7 2 13 6V13H1Z" fill="#fff"/></svg>Warehouses</li>
    <li><svg viewBox="0 0 14 14"><path d="M2 12 7 3 12 12Z" fill="#fff"/></svg>SLED</li>
    <li><svg viewBox="0 0 14 14"><circle cx="4" cy="4" r="2" fill="#fff"/><circle cx="10" cy="4" r="2" fill="#fff"/><rect x="2" y="7" width="4" height="6" fill="#fff"/><rect x="8" y="7" width="4" height="6" fill="#fff"/></svg>K-12</li>
    <li><svg viewBox="0 0 14 14"><rect x="1" y="3" width="12" height="10" fill="#fff"/><path d="M6 5h2v2h2v2H8v2H6V9H4V7h2Z" fill="#3fb2f2"/></svg>Medical / Hospitals</li>
    <li><svg viewBox="0 0 14 14"><rect x="3" y="1" width="8" height="12" fill="#fff"/></svg>Enterprise F1000</li>
    <li><svg viewBox="0 0 14 14"><path d="M3 1V13M3 2H11L9 5 11 8H3" stroke="#fff" stroke-width="1.5" fill="#fff"/></svg>Sports Venues</li>
    <li><svg viewBox="0 0 14 14"><path d="M1 4C4 7 10 7 13 4V12H1Z" fill="#fff"/></svg>Stadiums</li>
    <li><svg viewBox="0 0 14 14"><rect x="3" y="1" width="8" height="12" fill="#fff"/><rect x="5" y="3" width="1.5" height="1.5" fill="#3fb2f2"/><rect x="7.5" y="3" width="1.5" height="1.5" fill="#3fb2f2"/></svg>Hotels</li>
    <li><svg viewBox="0 0 14 14"><rect x="1" y="5" width="12" height="8" fill="#fff"/><path d="M1 5 3 1H11L13 5Z" fill="#fff"/></svg>Retail stores</li>
  </ul>

  <section class="info-column">
    <div class="info-block">
      <h2>WHAT IS A WIRELESS SITE SURVEY OR HEAT MAP?</h2>
      <p>A wireless site survey is a compilation of reports showing a visual representation of health of your wireless network. This does not only show how strong or weak a wireless signal is in any location it also helps aid in channel and placement to ensure maximum stable data rates are archived even where the single appears strong.</p>
    </div>
    <div class="info-block">
      <h2>WHY DO CUSTOMERS NEED A SITE SURVEY?</h2>
      <p>Any variety of factors can contribute to an unhealthy wireless network (electrical, motors, materials used in construction, distance, neighboring wireless networks, etc.) and traditional methods that use only blueprints and a computer program to show signal strength have shown to be ineffective.</p>
    </div>
    <div class="info-block">
      <h2>WHY SHOULD THEY USE YOU?</h2>
      <ol>
        <li><b>1.</b> 42% of businesses report some issues with wireless connectivity and acknowledge its effect on the bottom line*</li>
        <li><b>2.</b> Most of these problems are solved through either fine tuning the current equipment (managed services) or purchasing new equipment (incremental sales) of which you can provide both</li>
        <li><b>3.</b> Being a one-stop shop for all your customer's IT needs prevents them from needing additional vendors.</li>
        <li><b>4.</b> The increase of IoT (Internet of things) and BYOD (Bring Your Own Device)</li>
      </ol>
    </div>
  </section>

  <div class="brand">
    <div class="brand-mark"></div>
    <div class="brand-name">KESTREL</div>
    <div class="brand-contact">www.kestrelnet.com<br>info@kestrelnet.com</div>
    <div class="brand-phone">555-014-2290</div>
  </div>

  <div class="footer-bar"><span class="dark"></span><span class="blue"></span></div>
</main>
</body>
</html>
```